cold brew coffee bottle label "MOSS TIDE"

minimalist pastel coloured labels for cold brew coffee.
the name of the company is "MOSS TIDE".
would like the labels in multiple pastel colours: pink, blue, green, and yellow/beige.
prefer the use of the dubai font which can be downloaded from https://www.lorvatype.com/download
"MOSS TIDE" must be in a shiny gold.
"DUBAI" must be in a shiny gold.
attached are: the two types of bottles that will be used, some label examples that i have attempted to create, and some other cold brew bottle ideas i found on snapquilt. also i like the colors that are on the labels on the tin containers of coffee beans.
label should have area for bar code.
each label will have its colour correspond to the coffee origin, for example; green for Brazilian coffee, blue for Ethiopian coffee, pink for Mexican coffee. i would like the origin to be mentioned on the label as well.
the label should also have a "consume by:" section where the date can be stamped.
Updates

please provide landscape and portrait designs as it is not decided which will be used yet Added Monday, September 11, 2017

Industry/Entity Type

It Company

Font styles to use
Other font styles liked:
• Dubai font

Requirements
Must have
• portrait and landscape designs.
• Dubai fontarea for barcode.
• "consume by:" area

```html
<!DOCTYPE html>
<html lang="en">
<head>
<meta charset="utf-8">
<title>MOSS TIDE — Cold Brew Label</title>
<link rel="stylesheet" href="https://fonts.googleapis.com/css2?family=Open+Sans:wght@400;600&display=swap">
<style>
  :root {
    --backing: #c9c9c9;
    --mint: #97dccf;
    --white: #ffffff;
    --gold-light: #f2de00;
    --gold-dark: #c99400;
  }
  html, body {
    margin: 0;
    padding: 0;
    width: 1200px;
    height: 600px;
    overflow: hidden;
    background: var(--backing);
  }
  .label {
    position: relative;
    width: 1200px;
    height: 600px;
    background: var(--backing);
    font-family: "Open Sans", sans-serif;
  }
  .info-column {
    position: absolute;
    left: 0;
    top: 0;
    width: 300px;
    height: 600px;
  }
  .info-text {
    font-family: "Open Sans", sans-serif;
    font-weight: 400;
    fill: var(--mint);
    filter: drop-shadow(0 1px 0 rgba(0,0,0,0.18)) drop-shadow(0 -1px 0 rgba(255,255,255,0.35));
  }
  .info-text .origin-city {
    font-weight: 600;
    fill: url(#gold-fill);
  }
  .consume-by {
    font-family: "Open Sans", sans-serif;
    font-weight: 400;
    fill: var(--white);
  }
  .divider { fill: var(--mint); }
  .panel {
    position: absolute;
    left: 300px;
    width: 890px;
    background: var(--mint);
  }
  .panel-brand { top: 10px; height: 288px; }
  .panel-origin {
    top: 310px;
    height: 280px;
    display: flex;
    align-items: center;
    justify-content: center;
  }
  .brand-name {
    position: absolute;
    inset: 0;
  }
  .brand-name text {
    font-family: "Open Sans", sans-serif;
    font-weight: 600;
    fill: url(#gold-fill-brand);
    filter: drop-shadow(0 2px 1px rgba(120,90,0,0.35));
  }
  .origin-line {
    margin: 8px 0 0;
    font-family: "Open Sans", sans-serif;
    font-weight: 400;
    font-size: 64px;
    letter-spacing: 1px;
    color: var(--white);
    text-shadow: 0 2px 1px rgba(0,0,0,0.18);
  }
</style>
</head>
<body>
<main class="label">
  <svg class="info-column" width="300" height="600" viewBox="0 0 300 600">
    <defs>
      <linearGradient id="gold-fill" x1="0" y1="0" x2="0" y2="1">
        <stop offset="0" stop-color="#f2de00"/>
        <stop offset="1" stop-color="#c99400"/>
      </linearGradient>
    </defs>
    <text class="info-text" x="18" y="47" font-size="36" textLength="264" lengthAdjust="spacingAndGlyphs">SINGLE ORIGIN</text>
    <text class="info-text" x="18" y="84" font-size="40" textLength="264" lengthAdjust="spacingAndGlyphs">COLD BREW</text>
    <text class="info-text" x="18" y="133" font-size="56" textLength="264" lengthAdjust="spacingAndGlyphs">ROASTED</text>
    <text class="info-text" x="18" y="176" font-size="48" textLength="264" lengthAdjust="spacingAndGlyphs">&amp; BREWED</text>
    <text class="info-text" x="18" y="227" font-size="56" textLength="264" lengthAdjust="spacingAndGlyphs">IN <tspan class="origin-city">DUBAI</tspan></text>
    <rect class="divider" x="18" y="245" width="282" height="8"/>
    <text class="info-text" x="18" y="300" font-size="54" textLength="264" lengthAdjust="spacingAndGlyphs">READY TO</text>
    <text class="info-text" x="18" y="342" font-size="54" textLength="264" lengthAdjust="spacingAndGlyphs">CONSUME</text>
    <rect class="divider" x="18" y="348" width="282" height="8"/>
    <text class="info-text" x="18" y="400" font-size="48" textLength="264" lengthAdjust="spacingAndGlyphs">CONTAINS:</text>
    <text class="info-text" x="18" y="452" font-size="62" textLength="264" lengthAdjust="spacingAndGlyphs">COFFEE</text>
    <text class="info-text" x="18" y="503" font-size="58" textLength="264" lengthAdjust="spacingAndGlyphs">&amp;WATER</text>
    <text class="consume-by" x="18" y="525" font-size="20" textLength="172" lengthAdjust="spacingAndGlyphs">CONSUME BY:</text>
  </svg>

  <section class="panel panel-brand">
    <svg class="brand-name" width="890" height="288" viewBox="0 0 890 288">
      <defs>
        <linearGradient id="gold-fill-brand" x1="0" y1="0" x2="0" y2="1">
          <stop offset="0.3" stop-color="#f2de00"/>
          <stop offset="0.7" stop-color="#c99400"/>
        </linearGradient>
      </defs>
      <text x="105" y="200" font-size="123" textLength="685" lengthAdjust="spacingAndGlyphs">MOSS TIDE</text>
    </svg>
  </section>

  <section class="panel panel-origin">
    <p class="origin-line">single origin coffee</p>
  </section>
</main>
</body>
</html>
```